Flyer for the Harvest of lanterns conference

Flyer design for an annual international conference called "VELMARK 2017". This is a conference for young adults, so we hope to produce a design that is both professional and appealing to young people in general

We'd like the flyer to showcase the conference brand logo, and clearly highlight the key information to people who will read it.

Target Market(s)

Young people, young adults

Industry/Entity Type

Religious

Font styles to use
Sans Serif

Colors

Designer to choose colors to be used in the design.

Requirements
Must have
• - Should be only one page (Vertical or Horizontal).
• - the VELMAK logo and all the information found in the attached text file. This includes: Main topic: Your sons and daughters shall prophesy,
• Dates and time, location, contact information and everything that is in the attached text file.
Nice to have
• It would be nice to see samples where the white logo is used and another where the black one is used.
Should not have
• This is NOT a folded flyer, we will be sticking it on doors and public places. And we will be printing large simple to put on walls. So only one page with few words like an add (the words are in the attached file)

```html
<!DOCTYPE html>
<html lang="en">
<head>
<meta charset="utf-8">
<title>Harvest of Lanterns Conference – VELMARK 2017</title>
<link rel="stylesheet" href="https://fonts.googleapis.com/css2?family=Oswald:wght@500;600;700&family=Open+Sans:wght@600;700&family=Lobster&display=swap">
<style>
  :root {
    --gold: #e9b124;
    --gold-deep: #c8921a;
    --ink: #141414;
    --night: #1b1713;
    --paper: #ffffff;
    --mist: #ecedf0;
    --stage: #e6e3de;
  }
  * { margin: 0; padding: 0; box-sizing: border-box; }
  html, body { width: 1200px; height: 1200px; overflow: hidden; }
  body { background: var(--stage); position: relative; font-family: "Open Sans", sans-serif; }

  .flyer {
    position: absolute; left: 199px; top: 55px;
    width: 802px; height: 1090px; overflow: hidden;
    background: linear-gradient(160deg, var(--paper) 0%, var(--mist) 60%, #dfe1e5 100%);
    box-shadow: 0 8px 30px rgba(0,0,0,.25);
  }

  .hero-photo {
    position: absolute; left: 0; top: 0; width: 802px; height: 484px;
    background:
      radial-gradient(ellipse at 75% 30%, rgba(120,95,70,.55), transparent 60%),
      radial-gradient(ellipse at 30% 70%, rgba(80,62,46,.5), transparent 55%),
      linear-gradient(180deg, #0f0d0b 0%, #2a221b 55%, #1a1612 100%);
  }
  .swooshes { position: absolute; left: 0; top: 484px; width: 802px; height: 450px; }

  .edition {
    position: absolute; left: 83px; top: 57px; width: 319px; height: 57px;
  }
  .edition svg { position: absolute; inset: 0; }
  .edition span {
    position: relative; display: block; text-align: center; line-height: 57px;
    font-family: "Oswald", sans-serif; font-weight: 600; font-size: 38px; color: var(--ink);
    letter-spacing: .5px;
  }

  .brand { position: absolute; left: 560px; top: 44px; width: 212px; text-align: center; }
  .brand-dot {
    width: 110px; height: 110px; margin: 0 auto 12px; border-radius: 50%;
    border: 4px solid var(--gold);
  }
  .brand-name {
    font-family: "Oswald", sans-serif; font-weight: 500; font-size: 34px;
    color: var(--paper); letter-spacing: 4px; line-height: 1;
  }

  .headline {
    position: absolute; left: 32px; top: 155px; width: 423px; height: 226px;
    color: var(--paper); text-align: center;
  }
  .corner { position: absolute; width: 18px; height: 22px; border: 0 solid var(--paper); }
  .corner.tl { left: 0; top: 0; border-left-width: 3px; border-top-width: 3px; }
  .corner.tr { right: 0; top: 0; border-right-width: 3px; border-top-width: 3px; }
  .corner.bl { left: 0; bottom: 0; border-left-width: 3px; border-bottom-width: 3px; }
  .corner.br { right: 0; bottom: 0; border-right-width: 3px; border-bottom-width: 3px; }
  .headline p { line-height: 1; white-space: nowrap; }
  .headline .line-title { font-family: "Oswald", sans-serif; font-weight: 600; font-size: 41px; margin-top: 10px; }
  .headline .line-conf { font-family: "Oswald", sans-serif; font-weight: 600; font-size: 51px; margin-top: 6px; }
  .headline .line-script { font-family: "Lobster", cursive; font-size: 48px; margin-top: 2px; }
  .headline .line-verse { font-family: "Open Sans", sans-serif; font-weight: 600; font-size: 40px; margin-top: 8px; letter-spacing: .5px; }
  .gold { color: var(--gold); }

  .portrait {
    position: absolute; left: 405px; top: 400px; width: 400px; height: 400px;
  }
  .portrait-ring { position: absolute; inset: 0; }
  .portrait-photo {
    position: absolute; left: 18px; top: 18px; width: 364px; height: 364px; border-radius: 50%;
    border: 7px solid var(--paper);
    background:
      radial-gradient(circle at 68% 42%, #e8d9cf 0%, #c9b8ad 18%, transparent 36%),
      radial-gradient(circle at 25% 70%, #3d4250 0%, transparent 40%),
      linear-gradient(135deg, #b8c6d3 0%, #8f9caa 45%, #dfe4ea 100%);
  }

  .tag {
    position: absolute; height: 36px; padding-left: 30px;
    font-family: "Oswald", sans-serif; font-weight: 600; font-size: 23px; line-height: 36px;
    color: var(--ink);
  }
  .tag svg { position: absolute; left: 0; top: 0; z-index: 0; }
  .tag span { position: relative; }
  .tag-speakers { left: 11px; top: 510px; width: 205px; }
  .tag-date { left: 17px; top: 754px; width: 201px; }

  .speakers { position: absolute; left: 31px; top: 572px; list-style: none; }
  .speakers li {
    display: flex; align-items: center; gap: 9px; height: 32.3px;
    font-weight: 600; font-size: 19px; color: var(--ink);
  }
  .icon { flex: none; }

  .schedule { position: absolute; left: 31px; top: 812px; font-weight: 600; font-size: 19px; color: var(--ink); }
  .schedule .row { display: flex; align-items: flex-start; gap: 9px; line-height: 31.5px; }
  .schedule .row .icon { margin-top: 7px; }

  .contact-tab { position: absolute; left: 281px; top: 894px; width: 250px; height: 60px; z-index: 2; }
  .contact-tab svg { position: absolute; inset: 0; }
  .contact-tab span {
    position: relative; display: block; text-align: center; line-height: 62px;
    font-family: "Oswald", sans-serif; font-weight: 600; font-size: 24px; color: var(--ink);
  }

  .contact-bar {
    position: absolute; left: 0; top: 925px; width: 802px; height: 95px; background: var(--ink);
    display: flex; align-items: flex-end; justify-content: center; gap: 16px; padding-bottom: 17px;
    font-family: "Oswald", sans-serif; font-weight: 500; font-size: 25px; color: var(--paper);
  }
  .contact-item { display: flex; align-items: center; gap: 7px; white-space: nowrap; }

  .venue {
    position: absolute; left: 0; top: 1020px; width: 802px; height: 70px; background: var(--paper);
    text-align: center; padding-top: 11px;
    font-weight: 700; font-size: 16.5px; line-height: 22px; color: var(--ink);
  }
  .venue .icon { vertical-align: -2px; margin-right: 3px; }
</style>
</head>
<body>
<main class="flyer">
  <div class="hero-photo" role="img" aria-label="Dim conference hall with a speaker addressing a seated audience"></div>

  <svg class="swooshes" viewBox="0 0 802 450" aria-hidden="true">
    <path d="M0 300 C 200 250 380 330 560 420 L 0 450 Z" fill="#e2e4e8"/>
    <path d="M0 180 C 220 200 360 300 470 450 L 420 450 C 330 320 200 230 0 210 Z" fill="#ffffff" opacity=".8"/>
    <path d="M120 450 C 260 380 420 380 560 440 L 560 450 Z" fill="#d6d8dd"/>
    <path d="M0 10 L 420 0 L 230 40 Z" fill="#f6f6f7"/>
  </svg>

  <div class="edition">
    <svg width="319" height="57" viewBox="0 0 319 57" aria-hidden="true">
      <polygon points="0,0 319,0 303,28.5 319,57 0,57 16,28.5" fill="#ffffff"/>
    </svg>
    <span>VELMARK 2017</span>
  </div>

  <div class="brand">
    <div class="brand-dot"></div>
    <p class="brand-name">VELMAK</p>
  </div>

  <div class="headline">
    <i class="corner tl"></i><i class="corner tr"></i><i class="corner bl"></i><i class="corner br"></i>
    <p class="line-title">HARVEST <span class="gold">OF LANTERNS</span></p>
    <p class="line-conf"><span class="gold">CONFERENCE</span> YOUR</p>
    <p class="line-script">Sons &amp; <span class="gold">Daughters</span></p>
    <p class="line-verse"><span class="gold">SHALL</span> PROPHESY</p>
  </div>

  <div class="portrait">
    <svg class="portrait-ring" viewBox="0 0 400 400" aria-hidden="true">
      <circle cx="200" cy="200" r="197" fill="#ffffff"/>
      <path d="M 40 330 A 197 197 0 0 0 330 348" fill="none" stroke="#e9b124" stroke-width="10"/>
    </svg>
    <div class="portrait-photo" role="img" aria-label="Smiling young professional at a laptop in a bright meeting room with colleagues behind"></div>
  </div>

  <div class="tag tag-speakers">
    <svg width="205" height="36" viewBox="0 0 205 36" aria-hidden="true"><polygon points="0,0 205,0 187,18 205,36 0,36" fill="#e9b124"/></svg>
    <span>SPEAKERS :</span>
  </div>

  <ul class="speakers">
    <li><svg class="icon" width="18" height="18" viewBox="0 0 18 18" aria-hidden="true"><rect x="1.5" y="2.5" width="13" height="13" rx="2" fill="none" stroke="#141414" stroke-width="2"/><path d="M5 9 L8 12 L16 3" fill="none" stroke="#141414" stroke-width="2.4"/></svg>Prophet Lucien Mbaye</li>
    <li><svg class="icon" width="18" height="18" viewBox="0 0 18 18" aria-hidden="true"><rect x="1.5" y="2.5" width="13" height="13" rx="2" fill="none" stroke="#141414" stroke-width="2"/><path d="M5 9 L8 12 L16 3" fill="none" stroke="#141414" stroke-width="2.4"/></svg>Bishop Samuel Tendai</li>
    <li><svg class="icon" width="18" height="18" viewBox="0 0 18 18" aria-hidden="true"><rect x="1.5" y="2.5" width="13" height="13" rx="2" fill="none" stroke="#141414" stroke-width="2"/><path d="M5 9 L8 12 L16 3" fill="none" stroke="#141414" stroke-width="2.4"/></svg>Prophet Joseph Amani Lukusa</li>
    <li><svg class="icon" width="18" height="18" viewBox="0 0 18 18" aria-hidden="true"><rect x="1.5" y="2.5" width="13" height="13" rx="2" fill="none" stroke="#141414" stroke-width="2"/><path d="M5 9 L8 12 L16 3" fill="none" stroke="#141414" stroke-width="2.4"/></svg>Prophet Remy Kasongo</li>
    <li><svg class="icon" width="18" height="18" viewBox="0 0 18 18" aria-hidden="true"><rect x="1.5" y="2.5" width="13" height="13" rx="2" fill="none" stroke="#141414" stroke-width="2"/><path d="M5 9 L8 12 L16 3" fill="none" stroke="#141414" stroke-width="2.4"/></svg>Prophet Noel Ilunga</li>
  </ul>

  <div class="tag tag-date">
    <svg width="201" height="36" viewBox="0 0 201 36" aria-hidden="true"><polygon points="0,0 201,0 183,18 201,36 0,36" fill="#e9b124"/></svg>
    <span>DATE &amp; TIME</span>
  </div>

  <div class="schedule">
    <div class="row">
      <svg class="icon" width="19" height="18" viewBox="0 0 19 18" aria-hidden="true"><rect x="1" y="3" width="17" height="14" rx="1.5" fill="none" stroke="#141414" stroke-width="1.8"/><rect x="1" y="3" width="17" height="4" fill="#141414"/><path d="M5 1 V5 M14 1 V5 M4 10 H15 M4 13.5 H15 M7.5 8 V16 M11.5 8 V16" stroke="#141414" stroke-width="1.4"/></svg>
      <p>September 1st, 2nd and<br>3rd 2017 Start</p>
    </div>
    <div class="row">
      <svg class="icon" width="18" height="18" viewBox="0 0 18 18" aria-hidden="true"><circle cx="9" cy="9" r="7" fill="none" stroke="#141414" stroke-width="2.2"/><path d="M9 5 V9 H12" fill="none" stroke="#141414" stroke-width="2"/></svg>
      <p>6:00PM</p>
    </div>
  </div>

  <div class="contact-tab">
    <svg width="250" height="60" viewBox="0 0 250 60" aria-hidden="true"><polygon points="8,0 242,0 250,31 0,31" fill="#c8921a"/><rect x="8" y="0" width="234" height="60" fill="#e9b124"/></svg>
    <span>CONTACT INFO:</span>
  </div>

  <div class="contact-bar">
    <span class="contact-item"><svg class="icon" width="22" height="22" viewBox="0 0 22 22" aria-hidden="true"><path d="M5 2 L8.5 2 L10 7 L7.5 9 C9 12.5 10.5 14 13.5 15 L15.5 12.5 L20 14 L20 17.5 C20 19 18.5 20 17 20 C9 19 3 13 2 5 C2 3.5 3.5 2 5 2 Z" fill="#ffffff"/></svg>+1 (555) 014 2738</span>
    <span class="contact-item"><svg class="icon" width="24" height="18" viewBox="0 0 24 18" aria-hidden="true"><rect x="1.5" y="1.5" width="21" height="15" rx="1.5" fill="none" stroke="#ffffff" stroke-width="2"/><path d="M2 2.5 L12 10 L22 2.5" fill="none" stroke="#ffffff" stroke-width="2"/></svg>@lanternhall.org</span>
    <span class="contact-item"><svg class="icon" width="22" height="22" viewBox="0 0 22 22" aria-hidden="true"><rect x="1.5" y="8" width="11" height="6" rx="3" transform="rotate(45 7 11)" fill="none" stroke="#ffffff" stroke-width="2"/><rect x="9.5" y="8" width="11" height="6" rx="3" transform="rotate(45 15 11)" fill="none" stroke="#ffffff" stroke-width="2"/></svg>velmak.org</span>
  </div>

  <div class="venue">
    <p><svg class="icon" width="12" height="16" viewBox="0 0 12 16" aria-hidden="true"><path d="M6 1 C3 1 1 3.2 1 6 C1 9.5 6 15 6 15 C6 15 11 9.5 11 6 C11 3.2 9 1 6 1 Z" fill="none" stroke="#141414" stroke-width="2"/><circle cx="6" cy="6" r="1.8" fill="#141414"/></svg>Harborview Lantern Inn 410 Shore Avenue South Portland, ME 04101 United<br>States Room: Cedar Ball room</p>
  </div>
</main>
</body>
</html>
```